Supplement Rebranding Bottle Design

READ WORD DOCUMENT ATTACHED.
We want to rebrand our current health supplements (see below). We do want it to be modern, vibrant and appealing. Very upscale and elegant as it targets primarily women.
Bottle size: see pictures for bottle size, along with sample bottles that we like; we’re open to any bottle similar to the ones attached.
Current bottles: So ideally, we’d keep the core color on each bottle with a new branding/bottle design. But we're open to your suggestion.

Target Market(s)

mostly women but shouldn't be overly feminine

Requirements
Must have
• see bottle sizes attached

```html
<!DOCTYPE html>
<html lang="en">
<head>
<meta charset="utf-8">
<title>Pulse Supplement Range</title>
<link rel="stylesheet" href="https://fonts.googleapis.com/css2?family=Montserrat:wght@300;400;500&display=swap">
<style>
  :root {
    --bg: #ffffff;
    --ink: #ffffff;
    --liver-body: #4a138a;
    --liver-body-light: #7a2fd0;
    --liver-cap: #c99be6;
    --tummy-body: #5e0f0c;
    --tummy-body-light: #a32a22;
    --tummy-cap: #e6a09d;
    --hormone-body: #0c3a27;
    --hormone-body-light: #1f7a52;
    --hormone-cap: #8adcbb;
    --sugar-body: #161c4a;
    --sugar-body-light: #2e3a80;
    --sugar-cap: #aab0d8;
  }
  * { margin: 0; padding: 0; box-sizing: border-box; }
  html, body { width: 1200px; height: 654px; overflow: hidden; background: var(--bg); }
  body { position: relative; font-family: "Montserrat", sans-serif; color: var(--ink); }

  .bottle { position: absolute; top: 105px; width: 232px; height: 448px; }
  .bottle--liver   { left: 87px;  --body: var(--liver-body);   --body-light: var(--liver-body-light);   --cap: var(--liver-cap); }
  .bottle--tummy   { left: 345px; --body: var(--tummy-body);   --body-light: var(--tummy-body-light);   --cap: var(--tummy-cap); }
  .bottle--hormone { left: 612px; --body: var(--hormone-body); --body-light: var(--hormone-body-light); --cap: var(--hormone-cap); }
  .bottle--sugar   { left: 883px; --body: var(--sugar-body);   --body-light: var(--sugar-body-light);   --cap: var(--sugar-cap); }

  .cap { position: absolute; left: 20px; top: 0; width: 191px; height: 66px; border-radius: 10px 10px 4px 4px; background: var(--cap); }
  .neck { position: absolute; left: 30px; top: 64px; width: 171px; height: 32px; border-radius: 6px; background: var(--body); }
  .label {
    position: absolute; left: 0; top: 87px; width: 232px; height: 361px;
    border-radius: 60px 60px 34px 34px;
    background: linear-gradient(90deg, var(--body) 0%, var(--body) 55%, var(--body-light) 100%);
  }

  .name {
    position: absolute; left: 26px; top: 64px;
    font-size: 27px; font-weight: 400; line-height: 1; white-space: nowrap;
  }
  .line-name {
    position: absolute; left: 26px; top: 100px;
    font-size: 11px; font-weight: 500; letter-spacing: 4px; line-height: 1;
  }

  .details { position: absolute; left: 26px; top: 148px; width: 190px; font-weight: 300; }
  .tagline { font-size: 13px; line-height: 16px; height: 64px; }
  .rule { width: 18px; height: 1px; margin-top: 12px; background: var(--ink); }
  .kind { margin-top: 14px; font-size: 11px; line-height: 14px; }
  .count { margin-top: 18px; display: flex; align-items: center; gap: 4px; white-space: nowrap; }
  .count__num { font-size: 24px; font-weight: 300; line-height: 1; }
  .count__unit { font-size: 7px; line-height: 9px; letter-spacing: 0.3px; }
</style>
</head>
<body>
  <div class="bottle bottle--liver">
    <div class="cap"></div><div class="neck"></div>
    <div class="label">
      <p class="name">Liver</p>
      <p class="line-name">PULSE</p>
      <div class="details">
        <p class="tagline">Rejuvenating<br>Cleanse &amp; Detox<br>Formula*</p>
        <div class="rule"></div>
        <p class="kind">Dietary<br>Supplement</p>
        <p class="count"><span class="count__num">120</span><span class="count__unit">VEGETABLE<br>CAPSULES</span></p>
      </div>
    </div>
  </div>

  <div class="bottle bottle--tummy">
    <div class="cap"></div><div class="neck"></div>
    <div class="label">
      <p class="name">Tummy</p>
      <p class="line-name">PULSE</p>
      <div class="details">
        <p class="tagline">Oxygenating<br>Colon Cleanse*</p>
        <div class="rule"></div>
        <p class="kind">Dietary<br>Supplement</p>
        <p class="count"><span class="count__num">90</span><span class="count__unit">VEGETABLE<br>CAPSULES</span></p>
      </div>
    </div>
  </div>

  <div class="bottle bottle--hormone">
    <div class="cap"></div><div class="neck"></div>
    <div class="label">
      <p class="name">Hormone</p>
      <p class="line-name">PULSE</p>
      <div class="details">
        <p class="tagline">Supports<br>Healthy<br>Hormone<br>Levels*</p>
        <div class="rule"></div>
        <p class="kind">Dietary<br>Supplement</p>
        <p class="count"><span class="count__num">60</span><span class="count__unit">VEGETABLE<br>CAPSULES</span></p>
      </div>
    </div>
  </div>

  <div class="bottle bottle--sugar">
    <div class="cap"></div><div class="neck"></div>
    <div class="label">
      <p class="name">Blood Sugar</p>
      <p class="line-name">PULSE</p>
      <div class="details">
        <p class="tagline">Supports<br>Healthy Blood<br>Glucose Levels*</p>
        <div class="rule"></div>
        <p class="kind">Dietary<br>Supplement</p>
        <p class="count"><span class="count__num">60</span><span class="count__unit">VEGETABLE<br>CAPSULES</span></p>
      </div>
    </div>
  </div>
</body>
</html>
```